SkyvoraQ Business Cards and Stationary Design

Need a design for our business cards and stationary. I want to carry on the theme of the logo. I want the business cards to have a design on the back. I would like the business cards and the stationary to carry the same theme, design scheme, and branding

Target Market(s)

Airlines and Maintenance Facilities

Industry/Entity Type

Aviation

Contact Information for Business Card

Name
Position Title
Address: 4827 Tollbeck Lane, Fort Pierce, Florida, 34951
Office Number
Mobile Number
Email
Website

Font styles to use
Serif
Sans Serif

Colors

Designer to choose colors to be used in the design.

```html
<!DOCTYPE html>
<html lang="en">
<head>
<meta charset="utf-8">
<title>SkyvoraQ Business Card</title>
<link rel="stylesheet" href="https://fonts.googleapis.com/css2?family=Arimo:wght@400;700&display=swap">
<style>
  :root {
    --canvas: #ececec;
    --navy-deep: #1f1650;
    --brand-purple: #2a1a6e;
    --paper: #ffffff;
    --card-edge: #d9d9e0;
  }
  * { margin: 0; padding: 0; box-sizing: border-box; }
  html, body { width: 1200px; height: 1200px; overflow: hidden; }
  body {
    background: var(--canvas);
    font-family: "Arimo", Arial, sans-serif;
    position: relative;
  }
  .card {
    position: absolute;
    left: 180px;
    width: 840px;
    height: 480px;
    overflow: hidden;
    box-shadow: 0 6px 18px rgba(0,0,0,0.15);
  }
  /* Back of card */
  .card-back {
    top: 90px;
    background: var(--navy-deep);
    display: flex;
    flex-direction: column;
    align-items: center;
    justify-content: center;
    gap: 26px;
  }
  .card-back .brand-dot {
    width: 84px; height: 84px;
    border-radius: 50%;
    background: var(--paper);
  }
  .card-back .brand-name {
    color: var(--paper);
    font-weight: 700;
    font-size: 44px;
    letter-spacing: 10px;
    text-transform: uppercase;
  }
  /* Front of card */
  .card-front {
    top: 630px;
    background: var(--paper);
    border: 1px solid var(--card-edge);
  }
  .card-front svg.front-art { position: absolute; inset: 0; }
  .front-brand-top {
    position: absolute;
    top: 26px; right: 34px;
    display: flex; align-items: center; gap: 12px;
    color: var(--brand-purple);
    font-weight: 700;
    font-size: 26px;
    letter-spacing: 5px;
    text-transform: uppercase;
  }
  .front-brand-top .brand-dot {
    width: 30px; height: 30px; border-radius: 50%;
    background: var(--brand-purple);
  }
  .front-brand-lobe {
    position: absolute;
    left: 40px; top: 222px;
    width: 260px;
    text-align: center;
    color: var(--brand-purple);
    font-weight: 700;
    font-size: 36px;
    letter-spacing: 3px;
  }
  .contact {
    position: absolute;
    left: 430px; top: 140px;
    color: var(--paper);
  }
  .contact .person-name {
    font-weight: 700;
    font-size: 50px;
    line-height: 1;
    margin-bottom: 12px;
    text-transform: uppercase;
  }
  .contact .details {
    list-style: none;
    font-size: 25px;
    line-height: 1.22;
  }
</style>
</head>
<body>

  <section class="card card-back" aria-label="Business card back">
    <span class="brand-dot"></span>
    <span class="brand-name">SkyvoraQ</span>
  </section>

  <section class="card card-front" aria-label="Business card front">
    <svg class="front-art" viewBox="0 0 840 480" width="840" height="480" aria-hidden="true">
      <rect x="0" y="0" width="840" height="8" fill="var(--brand-purple)"/>
      <rect x="0" y="96" width="840" height="384" fill="var(--brand-purple)"/>
      <rect x="0" y="90" width="170" height="320" fill="var(--paper)"/>
      <circle cx="170" cy="240" r="190" fill="var(--paper)"/>
      <rect x="0" y="440" width="840" height="40" fill="var(--brand-purple)"/>
    </svg>

    <div class="front-brand-top"><span class="brand-dot"></span>SkyvoraQ</div>
    <div class="front-brand-lobe">SkyvoraQ</div>

    <div class="contact">
      <h1 class="person-name">Mara Linde</h1>
      <ul class="details">
        <li>MANAGER</li>
        <li>4827 Tollbeck Lane,</li>
        <li>Fort Pierce, Florida, 34951</li>
        <li>772 555 0148</li>
        <li>+1 772 555 0193</li>
        <li>mara@skyvoraq.com</li>
      </ul>
    </div>
  </section>

</body>
</html>
```